New design and logo for www.vornbuild.example

Hi, we need a new design for the site www.vornbuild.example
It's a scale modelling e-commerce website (no RC models or die cast models, only static models to build) which is a highly technical hobby (exact scale reproduction from passionated starting with the kit we sell using different material (paint, airbrush...)). Main fields are military aircrafts, military vehicles and scale figures. They are also less important fields like reference books, boats, civilian vehicles, tools like aibrushes, paints and so on.
Every scale model come with plans for mounting the items (mainly on plastic sprues), instructions for painting and most of them have decals to apply.
We don't want a military feeling, and visitors must understand immediately that our site is not about RC models or die cast models but are kits to build. They are not toys, customers are mainly adults aroud 30-50 (hobby starting aroud 14 years old), mainly mens but a few girls are in the hobby too (mainly in figures).
We would like to get rid of the right banner and have a search engine (actually on left top of the menu) and menu (actually on left) on all the pages. We need the main page banners for new products or announcements and the first page must show the last added product.
The product's list (click on any link on left) must be improved and the product's detail too.
Here are the page sample to make template for (same design but we need to know how to build them):
Main page: http://www.vornbuild.example/
Product's list: http://www.vornbuild.example/planes-1_48-aircraft-kits-c-21_27.html
Product's detail: http://www.vornbuild.example/pelmora-pm41827-1_48-halvener-hx-203b-kestrel-foreign-af-p-30059.html
Those items must be visible at any time (design can be changed without problem) :
The cart with content once you add something on it
The language seletor
The currency selector
social link 1 Like link
link to account
newsletter register form (actually not visible on our site, only a field for entering the email but should be appealing)
You are free to put all other informations (contact, general informations, payments...) where you want
Design must be done in a way it will improve the sales and feel confident with the site. We have no preferences for colors and disposition, new logo proposal is also highly welcome (with eventually an extra fee, but we won't start 2 projects).
If you have any question, please feel free to contact us.
Thank you for reading, do your best and good luck!
Target Market(s)
Mainly mens 30-50
Industry/Entity Type
E-Commerce
Requirements
Must have
- Understand it's a scale modeling site and not toy, die cast or RC
The language seletor
The currency selector
social link 1 Like link
link to account
Nice to have
- New logo

```html
<!DOCTYPE html>
<html lang="en">
<head>
<meta charset="utf-8">
<title>Vornbuild – Model Kits</title>
<link rel="stylesheet" href="https://fonts.googleapis.com/css2?family=Ubuntu:wght@400;500;700&display=swap">
<style>
:root{
  --gold:#e9a300;--gold-light:#f6c23a;--gold-dark:#c98a00;
  --ink:#333;--grey:#5b5b5b;--panel:#3b3b3b;--line:#ddd;--footer:#efefef;
}
*{box-sizing:border-box;margin:0;padding:0}
html,body{width:1200px;height:1080px;overflow:hidden;background:#fff;font-family:'Ubuntu',sans-serif;color:var(--ink)}
.canvas{position:relative;width:1200px;height:1080px}
.abs{position:absolute}
.topbar{left:0;top:0;width:1200px;height:27px;background:var(--grey);border-bottom:2px solid var(--gold);font-size:11px;color:#ddd}
.topbar .links{left:124px;top:7px;display:flex;gap:21px}
.topbar .ship{right:111px;top:7px;display:flex;align-items:center;gap:5px}
.flag{width:20px;height:12px;background:#2b3f8f;display:inline-block}
.logo{left:122px;top:55px;display:flex;align-items:center;gap:6px}
.logo .sq{width:20px;height:20px;background:var(--grey)}
.logo .name{font-size:38px;font-weight:700;color:var(--gold)}
.acct{right:111px;top:42px;font-size:11px;color:var(--gold)}
.acct span{color:#999;margin:0 6px}
.cart{left:968px;top:70px;width:122px;height:35px;border:1px solid var(--line);display:flex;align-items:center;padding-left:8px;gap:9px;font-size:12px;font-weight:700;color:var(--gold)}
.nav{left:109px;top:124px;width:981px;height:37px;background:linear-gradient(#f7c43c,#e7a100);display:flex;border:1px solid var(--gold-dark)}
.nav a{color:#fff;font-size:11.5px;font-weight:500;text-decoration:none;padding:0 5px;line-height:35px;border-right:1px solid rgba(255,255,255,.5);flex:1 1 auto;text-align:center;white-space:nowrap}
.nav a:last-child{border:0}
.hero{left:110px;top:172px;width:730px;height:299px;background:linear-gradient(#c4ad74 0%,#a89566 45%,#7f7551 62%,#bfae85 75%,#d4c39a 100%)}
.hero-title{left:110px;top:310px;height:57px;padding:0 12px;background:var(--gold);color:#fff;font-size:31px;font-weight:700;line-height:57px}
.hero-sub{left:110px;top:372px;height:46px;padding:0 12px;background:#111;color:#fff;font-size:17px;font-weight:700;line-height:46px;white-space:nowrap}
.dots{left:125px;top:445px;display:flex;gap:5px}
.dots i{width:9px;height:9px;border-radius:50%;background:#bbb;border:1px solid #666}
.dots i:first-child{background:#333}
.finder{left:850px;top:172px;width:240px;height:299px;background:var(--panel);border-radius:3px;text-align:center;color:#fff}
.finder h2{font-weight:400;font-size:18px;margin:21px 0 17px}
.field{margin:0 10px 21px;height:31px;background:#fff;border-radius:2px;color:#666;font-size:12px;text-align:left;padding:0 8px;line-height:31px;position:relative}
.field.sel::after{content:"";position:absolute;right:10px;top:11px;border:5px solid transparent;border-top:8px solid #999}
.field.sel::before{content:"";position:absolute;right:34px;top:6px;width:1px;height:19px;background:#ccc}
.btn{display:inline-block;background:linear-gradient(#f7c43c,#e29c00);color:#fff;font-size:12px;font-weight:500;border:1px solid var(--gold-dark);border-radius:3px;padding:0 9px;line-height:29px;white-space:nowrap}
.btn.dark{background:#222;border-color:#000}
.finder .btn{font-size:13px;line-height:32px;padding:0 11px}
.finder .adv{display:block;color:var(--gold);font-size:12px;margin-top:15px}
.heading{left:110px;top:483px;width:730px;height:39px;background:linear-gradient(#666,#3c3c3c);border:1px solid #222;color:#fff;font-size:17px;line-height:37px;padding-left:9px}
.card{width:160px;height:219px;border:1px solid var(--line);text-align:center;font-size:11px;color:#555}
.thumb{width:146px;height:97px;margin:7px auto 16px}
.t1{background:linear-gradient(#2a2418,#7b4a1c 50%,#1e1a14)}
.t2{background:linear-gradient(90deg,#e6e2d6,#a88a5a 50%,#e6e2d6)}
.t3{background:linear-gradient(#3c4f74,#6a7f9a 50%,#4a5a3a)}
.card p{line-height:16px;padding:0 10px}
.price{color:var(--gold);font-size:11.5px;font-weight:500}
.card .btn{margin-top:11px}
.side-h{width:240px;height:39px;background:linear-gradient(#f7c43c,#e29c00);color:#fff;font-size:17px;line-height:39px;padding-left:13px;border-radius:3px 3px 0 0}
.side-box{width:240px;border:1px solid var(--line);border-top:0;text-align:center;font-size:11px;color:#555}
.email{margin:14px 9px 8px;height:31px;border:1px solid var(--line);font-size:11px;text-align:left;padding-left:8px;line-height:29px}
.social{border-top:1px solid var(--line);margin:12px 0 0;padding:16px 0 0;display:flex;justify-content:center;gap:18px}
.social i{width:26px;height:26px;display:block}
.footer{left:0;top:1017px;width:1200px;height:63px;background:var(--footer);font-size:11.5px;color:#666}
.footer .fl{left:110px;top:12px}
.footer .fl span{margin:0 5px;color:#999}
.footer .copy{left:110px;top:36px;font-size:11px}
.pays{right:110px;top:22px;display:flex;gap:6px}
.pays span{width:37px;height:22px;border:1px solid #bbb;background:#fff;font-size:8.5px;font-weight:700;color:#345;text-align:center;line-height:20px}
</style>
</head>
<body>
<div class="canvas">
  <div class="abs topbar">
    <div class="abs links"><span>HOME</span><span>NEW PRODUCTS</span><span>SALES</span><span>PREORDER</span></div>
    <div class="abs ship">Shipping to <i class="flag"></i> GBP (£) Change</div>
  </div>

  <div class="abs logo"><i class="sq"></i><span class="name">Vornbuild</span></div>
  <div class="abs acct">MY ACCOUNT<span>|</span>CART CONTENTS<span>|</span>CHECKOUT</div>
  <div class="abs cart">
    <svg width="22" height="20" viewBox="0 0 22 20"><path d="M1 2h4l3 10h10l3-7H7" fill="none" stroke="#222" stroke-width="2"/><circle cx="9" cy="17" r="2" fill="#222"/><circle cx="17" cy="17" r="2" fill="#222"/></svg>
    MY CART:0 <svg width="9" height="6"><path d="M0 0h9L4.5 6z" fill="#ccc"/></svg>
  </div>

  <nav class="abs nav">
    <a>Destocking</a><a>Planes</a><a>AFV</a><a>Figurines</a><a>Car &amp; truck</a><a>Ship</a><a>Dioramas acc</a><a>Fiction</a><a>Books</a><a>Wargame</a><a>Swiss Air Force</a><a>Tools</a><a>Collections &amp; rarities</a><a>Second hand</a><a>Others</a>
  </nav>

  <div class="abs hero" role="img" aria-label="Photo of a camouflaged jet fighter parked on an airfield apron"></div>
  <div class="abs hero-title">VANTOR GR.1/GR.3</div>
  <div class="abs hero-sub">YOUR ONLINE SHOP FOR MODEL KITS AND DETAIL SETS.</div>
  <div class="abs dots"><i></i><i></i><i></i></div>

  <div class="abs finder">
    <h2>QUICK FINDER</h2>
    <div class="field">Enter Keyword(s):</div>
    <div class="field sel">Select Categories</div>
    <div class="field sel">Manufacturers</div>
    <span class="btn">FIND NOW!</span>
    <span class="adv">Advanced Search</span>
  </div>

  <div class="abs heading">NEW PRODUCTS</div>

  <div class="abs card" style="left:110px;top:543px"><div class="thumb t1" role="img" aria-label="Box art of a red triplane kit"></div><p>1/35 Russian Fuel Trailer 1 Axle</p><div class="price">CHF 19.10</div><span class="btn">ADD TO CART</span></div>
  <div class="abs card" style="left:300px;top:543px"><div class="thumb t2" role="img" aria-label="Photo of a built fuel trailer model"></div><p>1/35 Russian Fuel Trailer 1 Axle</p><div class="price">CHF 19.10</div><span class="btn">ADD TO CART</span></div>
  <div class="abs card" style="left:490px;top:543px"><div class="thumb t3" role="img" aria-label="Box art of a fighter aircraft in flight"></div><p>1/35 Russian Fuel Trailer 1 Axle</p><div class="price">CHF 19.10</div><span class="btn">ADD TO CART</span></div>
  <div class="abs card" style="left:680px;top:543px"><div class="thumb t1" role="img" aria-label="Box art of a red triplane kit"></div><p>1/35 Russian Fuel Trailer 1 Axle</p><div class="price">CHF 19.10</div><span class="btn">ADD TO CART</span></div>
  <div class="abs card" style="left:110px;top:774px"><div class="thumb t1" role="img" aria-label="Box art of a red triplane kit"></div><p>1/35 Russian Fuel Trailer 1 Axle</p><div class="price">CHF 19.10</div><span class="btn">ADD TO CART</span></div>
  <div class="abs card" style="left:300px;top:774px"><div class="thumb t2" role="img" aria-label="Photo of a built fuel trailer model"></div><p>1/35 Russian Fuel Trailer 1 Axle</p><div class="price">CHF 19.10</div><span class="btn">ADD TO CART</span></div>
  <div class="abs card" style="left:490px;top:774px"><div class="thumb t3" role="img" aria-label="Box art of a fighter aircraft in flight"></div><p>1/35 Russian Fuel Trailer 1 Axle</p><div class="price">CHF 19.10</div><span class="btn">ADD TO CART</span></div>
  <div class="abs card" style="left:680px;top:774px"><div class="thumb t1" role="img" aria-label="Box art of a red triplane kit"></div><p>1/35 Russian Fuel Trailer 1 Axle</p><div class="price">CHF 19.10</div><span class="btn">ADD TO CART</span></div>

  <div class="abs" style="left:850px;top:483px">
    <div class="side-h">What's New?</div>
    <div class="side-box" style="height:260px;padding-top:20px">
      <div class="thumb t1" style="width:146px;height:115px;margin:0 auto 17px" role="img" aria-label="Box art of a red triplane kit"></div>
      <p style="line-height:16px;padding:0 45px">1/35 Russian Fuel Trailer 1 Axle</p>
      <div class="price">CHF 19.10</div>
      <span class="btn dark" style="margin-top:10px">ADD TO CART</span>
    </div>
  </div>

  <div class="abs" style="left:850px;top:793px">
    <div class="side-h">Tell A Friend</div>
    <div class="side-box" style="height:160px">
      <div class="email">Enter Email Here</div>
      <span class="btn">SUBMIT</span>
      <div class="social">
        <i style="background:#3b5aa0" role="img" aria-label="Social link 1"></i>
        <i style="background:#2aa7e0" role="img" aria-label="Social link 2"></i>
        <i style="background:#c4231b" role="img" aria-label="Social link 3"></i>
        <i style="background:#d34836" role="img" aria-label="Social link 4"></i>
      </div>
    </div>
  </div>

  <footer class="abs footer">
    <div class="abs fl">About Us<span>|</span>Sitemap<span>|</span>Help / FAQs<span>|</span>Order Status<span>|</span>Returns<span>|</span>Contact Us</div>
    <div class="abs copy">Copyright © 2008-2013 Vornbuild | All Rights Reserved.</div>
    <div class="abs pays"><span>Payora</span><span>Trivo</span><span>Cardex</span><span>Bank</span><span>Novus</span><span>Coresta</span></div>
  </footer>
</div>
</body>
</html>
```